Package Design for a Grow Your Own Bonsai tree kit

I would like a package redesign of a bonsai tree kit I currently sell. I want it to look modern unique and beautiful. It’s a gift item, so the way the box is presented is important.

I plan to launch several similar plant kits so would like a design that’s transferable to other products. I’d like to incorporate the colour green-and browns - naturalcolours

Target Market(s)

The target market are millennials living in small spaces - without an out door garden or easy access to nature

Industry/Entity Type

Gardener

Font styles to use
Sans Serif

Colors
faa54b
00a990
9bcb3b

Requirements
Must have
• Fresh, clean modern look
Nice to have
• I have included 3 images of bonsai kits below. I like the 1st 2 pictures- they are original and professional and very appealing. The green and white product is my existing packaging. I want to look more professionally desgned

```html
<!DOCTYPE html>
<html lang="en">
<head>
<meta charset="utf-8">
<title>Bonsai Tree Kit – Seed Starter Pack</title>
<link href="https://fonts.googleapis.com/css2?family=Heebo:wght@900&family=Kaushan+Script&family=Roboto:wght@400;500&display=swap" rel="stylesheet">
<style>
  :root {
    --paper: #ffffff;
    --orange: #faa54b;
    --teal: #00a990;
    --leaf: #9bcb3b;
    --ink: #111111;
    --brand-ink: #2b3a3a;
    --foliage-light: #a9cf6a;
    --foliage-dark: #4f8a45;
    --bark: #9a8468;
    --pot: #a8623a;
  }
  * { margin: 0; padding: 0; box-sizing: border-box; }
  html, body { width: 1200px; height: 848px; overflow: hidden; background: var(--paper); }
  .package-front { position: relative; width: 1200px; height: 848px; background: var(--paper); overflow: hidden; }
  .bonsai-illustration { position: absolute; left: 70px; top: 118px; width: 552px; height: 620px; }
  .brush-layer { position: absolute; inset: 0; }
  .brand { position: absolute; left: 804px; top: 72px; display: flex; align-items: center; gap: 8px;
    font-family: "Roboto", sans-serif; font-weight: 400; font-size: 27px; color: var(--brand-ink); letter-spacing: 0.3px; }
  .brand-dot { width: 12px; height: 12px; border-radius: 50%; background: var(--leaf); }
  .title { position: absolute; left: 740px; top: 274px; width: 380px; }
  .title-main { display: block; font-family: "Heebo", sans-serif; font-weight: 900; font-size: 114px; line-height: 1;
    color: var(--leaf); letter-spacing: -1px; }
  .title-script { display: block; font-family: "Kaushan Script", cursive; font-size: 116px; line-height: 1;
    color: var(--ink); margin-top: 0; margin-left: 0; letter-spacing: 2px; }
  .pack-label { position: absolute; left: 760px; top: 604px; width: 300px; text-align: center;
    font-family: "Roboto", sans-serif; font-weight: 400; font-size: 19px; letter-spacing: 3px; color: var(--paper); }
  .feature-icons { position: absolute; left: 852px; top: 740px; display: flex; gap: 22px; }
  .feature-icons svg { width: 56px; height: 56px; }
</style>
</head>
<body>
<main class="package-front">
  <svg class="bonsai-illustration" viewBox="0 0 552 620" role="img" aria-label="Watercolour illustration of a bonsai tree with a twisting trunk and layered green foliage, planted in a brown clay pot">
    <defs>
      <linearGradient id="bonsaiTone" x1="0" y1="0" x2="0" y2="1">
        <stop offset="0" stop-color="var(--foliage-light)"/>
        <stop offset="0.55" stop-color="var(--foliage-dark)"/>
        <stop offset="0.78" stop-color="var(--bark)"/>
        <stop offset="1" stop-color="var(--pot)"/>
      </linearGradient>
    </defs>
    <rect x="0" y="0" width="552" height="620" rx="28" fill="url(#bonsaiTone)" opacity="0.9"/>
  </svg>

  <svg class="brush-layer" viewBox="0 0 1200 848" aria-hidden="true">
    <path class="stroke-orange" fill="var(--orange)" d="M478 0 L572 0 L560 20 L548 46 L530 78 L500 122 L478 150 L452 182 L420 220 L386 250 L352 276 L300 300 L248 318 L212 330 L170 340 L160 326 L200 306 L240 286 L282 262 L318 236 L350 204 L378 170 L404 132 L430 92 L452 54 L468 24 Z"/>
    <path class="stroke-teal" fill="var(--teal)" d="M0 384 L22 392 L48 416 L78 452 L110 500 L140 550 L172 604 L200 658 L228 712 L254 764 L274 808 L292 848 L240 848 L222 812 L200 770 L176 724 L150 678 L120 630 L88 584 L56 540 L26 504 L0 480 Z"/>
    <path class="stroke-leaf" fill="var(--leaf)" d="M1200 552 L1120 556 L1040 556 L980 560 L920 562 L860 568 L800 578 L740 590 L690 604 L640 620 L600 638 L560 654 L524 670 L494 690 L508 694 L540 684 L580 676 L620 670 L660 666 L700 662 L740 660 L790 660 L840 656 L900 652 L960 650 L1020 648 L1090 646 L1160 648 L1200 648 Z"/>
  </svg>

  <div class="brand"><span class="brand-name">Metro Sprout</span><span class="brand-dot"></span></div>

  <h1 class="title">
    <span class="title-main">Bonsai</span>
    <span class="title-script">tree kit</span>
  </h1>

  <p class="pack-label">SEED STARTER PACK</p>

  <div class="feature-icons">
    <svg viewBox="0 0 56 56" role="img" aria-label="Pruning shears">
      <g fill="none" stroke="var(--ink)" stroke-width="2.4" stroke-linecap="round" stroke-linejoin="round">
        <path d="M10 46 L30 26 L44 10"/>
        <path d="M22 50 L32 28 L48 16"/>
        <path d="M6 36 L24 30"/>
        <circle cx="31" cy="27" r="2"/>
      </g>
    </svg>
    <svg viewBox="0 0 56 56" role="img" aria-label="Potted tree">
      <g fill="none" stroke="var(--ink)" stroke-width="2.4" stroke-linecap="round" stroke-linejoin="round">
        <path d="M12 16 Q14 8 24 10 Q30 4 38 10 Q46 10 44 18 Z"/>
        <path d="M28 18 Q24 28 32 30 Q36 34 28 40"/>
        <path d="M10 40 L46 40 L42 50 L14 50 Z"/>
      </g>
    </svg>
  </div>
</main>
</body>
</html>
```